Lantern Walk! A website showcasing who I am as a person

Lantern Walk started out as idea for me to better myself as a person and work on small projects that would help me grow as a person. Now I want to build a website showcasing "Lantern Walk." I want the website to showcase who I am and how I have grown both professionally and personally. I can build the raw code of the website on my own but I am not really much of a designer. I am looking for a design where I can write and post blogs, articles and share my thoughts. A little about myself and the ideas and interests that I want to share
What is Lantern Walk
Who I am
Background - Professional
Brand Marketing
Email Automation
Hiking
Rock Climbing
Traveling
Exercising and Transformation
"Personal Thoughts"
Hopefully this is enough information to get people started on some designs.
Industry/Entity Type
Work
Number of Pages Required
3 page

```html
<!DOCTYPE html>
<html lang="en">
<head>
<meta charset="utf-8">
<title>Lantern Walk</title>
<link href="https://fonts.googleapis.com/css2?family=Roboto:wght@300;400;500;700&display=swap" rel="stylesheet">
<style>
:root{
  --blue:#2f6fb6;
  --blue-bright:#2f86dc;
  --dark:#2b3340;
  --ink:#1f2328;
  --muted:#8a9099;
  --paper:#f4f5f6;
  --white:#ffffff;
}
*{margin:0;padding:0;box-sizing:border-box}
html,body{width:1200px;height:4534px;overflow:hidden}
body{font-family:"Roboto",Arial,sans-serif;color:var(--ink);background:var(--white)}
.section{position:relative;width:1200px;overflow:hidden}
.abs{position:absolute}
a{color:inherit;text-decoration:none}
.underline-link{font-weight:500;font-size:17px;color:var(--white);padding-bottom:10px;border-bottom:3px solid var(--blue-bright)}

/* hero */
.hero{height:750px}
.hero-photo{position:absolute;top:0;height:750px;width:600px}
.hero-photo.left{left:0;background:linear-gradient(180deg,#9aa6b1 0%,#6b7784 45%,#3d4650 100%)}
.hero-photo.right{left:600px;background:linear-gradient(180deg,#a9b7c4 0%,#5f6f80 50%,#2d3844 100%)}
.hero-photo::after{content:"";position:absolute;inset:0;background:rgba(20,30,45,.25)}
.brand{left:112px;top:30px;font-size:32px;font-weight:700;color:var(--blue-bright);z-index:2}
.hero-social{right:110px;top:42px;display:flex;gap:26px;z-index:2}
.dot-icon{width:14px;height:14px;border-radius:50%;background:rgba(255,255,255,.85)}
.menu-btn{right:-18px;top:26px;width:70px;height:56px;border-radius:28px;background:var(--white);z-index:2}
.menu-btn span{position:absolute;left:18px;width:20px;height:3px;background:var(--ink)}
.hero-block{z-index:2;color:var(--white)}
.hero-block h2{font-size:46px;font-weight:700;margin-bottom:18px}
.hero-block p{font-size:18px;line-height:1.6;font-weight:400;margin-bottom:40px}
.hero-block.right{text-align:right}

/* about */
.about{height:750px;background:var(--blue);color:var(--white)}
.about h2{font-size:31px;font-weight:700}
.portrait{left:112px;width:333px;height:333px;background:linear-gradient(160deg,#b9a98f 0%,#8d7660 55%,#4f4237 100%)}
.portrait-social{left:290px;display:flex;gap:16px}
.portrait-social .dot-icon{width:10px;height:10px}
.about-bio{left:112px;width:340px;font-size:12.5px;line-height:1.75;font-weight:300}
.skills-title{left:588px;font-size:24px;font-weight:500}
.skills-title::after,.timeline-title::after,.memory-title::after,.journal-title::after{content:"";display:block;width:150px;height:3px;margin-top:10px;background:var(--white)}
.skill{left:588px;width:500px;display:flex;gap:26px}
.skill svg{flex:none}
.skill h3{font-size:14px;font-weight:500;letter-spacing:.3px;margin:2px 0 5px}
.skill p{font-size:12px;line-height:1.6;font-weight:300;opacity:.9}

/* timeline */
.timeline{height:563px;background:linear-gradient(180deg,#2e3744,#262e39)}
.timeline-title{left:112px;top:102px;font-size:24px;font-weight:500;color:var(--blue-bright)}
.timeline-title::after{width:140px;background:var(--white)}
.year-big{left:270px;top:230px;font-size:66px;font-weight:500;letter-spacing:3px;color:var(--blue-bright)}
.years{left:112px;top:398px;width:490px;display:flex;justify-content:space-between;font-size:15px;color:#6c7581;letter-spacing:1px}
.ticks{left:130px;top:428px;width:470px;height:30px}
.org-mark{left:695px;top:100px;display:flex;flex-direction:column;align-items:flex-start;gap:8px;color:var(--white);font-size:22px;font-weight:500;letter-spacing:1px}
.org-mark i{display:block;width:44px;height:44px;background:var(--white)}
.job{left:695px;top:218px;width:400px;color:#c4cad2}
.job h3{font-size:19px;font-weight:500;color:var(--blue-bright);letter-spacing:1.5px}
.job h3 small{font-size:14px;font-weight:400;letter-spacing:.5px}
.job h4{font-size:15px;font-weight:400;color:var(--white);letter-spacing:1px;margin:10px 0 22px}
.job p{font-size:13.5px;line-height:1.75;letter-spacing:.6px;color:#8d95a0}
.job a{display:inline-block;margin-top:28px;font-size:15px;color:var(--blue-bright);font-weight:500}

/* social feed */
.feed{height:332px;background:var(--paper)}
.post{top:72px;width:300px;height:160px;padding:16px 14px}
.post.raised{background:var(--white);box-shadow:0 4px 16px rgba(0,0,0,.12);top:62px;height:178px;padding:18px 18px}
.post-head{display:flex;align-items:center;gap:10px;font-size:14px;font-weight:500;color:var(--ink)}
.post-head i{width:20px;height:20px;border-radius:3px;background:var(--blue);display:block}
.post-head time{font-weight:400;font-size:12px;color:var(--muted)}
.post-head-top{margin-bottom:14px}
.post p{font-size:12.5px;line-height:1.65;color:var(--muted)}
.feed-dots{left:570px;top:282px;display:flex;gap:10px}
.feed-dots span{width:10px;height:10px;border-radius:50%;border:1.5px solid #999}
.feed-dots span.on{background:#333;border-color:#333}

/* memories */
.memory{height:745px;background:var(--blue);color:var(--white)}
.memory-title{left:112px;top:102px;font-size:27px;font-weight:500}
.memory-tabs{right:112px;top:108px;display:flex;gap:26px;font-size:15.5px;font-weight:500;align-items:center}
.photo{top:182px;height:438px}
.photo-caption{left:40px;bottom:44px}
.photo-caption h3{font-size:18px;font-weight:700;letter-spacing:1px}
.photo-caption p{font-size:13px;margin:6px 0 30px}
.photo-caption a{font-size:13px;color:var(--blue-bright);font-weight:500}
.arrow{top:640px}

/* journal */
.journal{height:740px;background:var(--paper)}
.journal-title{left:112px;top:104px;font-size:27px;font-weight:500}
.journal-title::after{background:var(--blue-bright);width:170px}
.all-posts{right:112px;top:110px;font-size:16px;font-weight:500}
.card{background:var(--white);box-shadow:0 2px 6px rgba(0,0,0,.06)}
.card h3{font-size:19px;font-weight:700;line-height:1.45}
.meta{display:flex;justify-content:space-between;font-size:13px;color:var(--muted);margin:12px 0 16px}
.card p{font-size:13px;line-height:1.7;color:var(--muted)}
.feature-dark{color:var(--white)}
.feature-dark .meta,.feature-dark p{color:#dfe3e8}

/* stats */
.stats{height:333px;background:var(--blue);color:var(--white)}
.stat{top:68px;width:260px;text-align:center}
.stat svg{display:block;margin:0 auto 28px}
.stat h3{font-size:16px;font-weight:500;margin-bottom:8px}
.stat p{font-size:12.5px;line-height:1.65;font-weight:300;opacity:.9}

/* footer */
.footer{height:321px;background:var(--dark);color:var(--white)}
.footer h2{font-size:32px;font-weight:700}
.footer .name{font-size:36px;font-weight:700;color:var(--blue-bright)}
.footer .role{font-size:17px;font-weight:500}
.footer-social{left:112px;top:232px;display:flex;gap:34px}
.footer-social .dot-icon{background:#7f8a98}
.subscribe{left:790px;top:64px;width:300px}
.subscribe h4{font-size:14px;font-weight:500;margin-bottom:14px}
.subscribe .field{width:235px;height:42px;border:1px solid #56606d;padding:12px;font-size:12px;color:#7f8a98}
.contact{margin-top:36px;font-size:12px;color:#7f8a98;line-height:1.7}
</style>
</head>
<body>

<header class="section hero">
  <div class="hero-photo left" role="img" aria-label="Man in a suit standing on a mountain ridge, seen from behind"></div>
  <div class="hero-photo right" role="img" aria-label="Hiker with a large backpack looking over mountain peaks"></div>
  <div class="abs brand">Lantern Walk.</div>
  <div class="abs hero-social"><i class="dot-icon"></i><i class="dot-icon"></i><i class="dot-icon"></i><i class="dot-icon"></i></div>
  <div class="abs menu-btn"><span style="top:20px"></span><span style="top:27px"></span><span style="top:34px"></span></div>
  <div class="abs hero-block" style="left:112px;top:410px;width:420px">
    <h2>Brand Marketing</h2>
    <p>at Norwell Partners, London with 7 years of experience in the field and has served 3 Top 500 Global companies</p>
    <a class="underline-link" href="#">Download Resume</a>
  </div>
  <div class="abs hero-block right" style="right:112px;top:410px;width:440px">
    <h2>Travel Enthusiast</h2>
    <p>I have travelled over 100 places of natural beauty in last 8 years. Capturing the natural beauty is my another hobby.</p>
    <a class="underline-link" href="#">Picture Gallary</a>
  </div>
</header>

<section class="section about">
  <h2 class="abs" style="left:112px;top:98px">Your Name</h2>
  <div class="abs portrait" style="top:162px" role="img" aria-label="Portrait photo of the site owner wearing sunglasses"></div>
  <div class="abs portrait-social" style="top:464px"><i class="dot-icon"></i><i class="dot-icon"></i><i class="dot-icon"></i><i class="dot-icon"></i></div>
  <p class="abs about-bio" style="top:528px">I am a 35 years old brand consultant and travel enthusiast. Presently I am working as a self-employed at Edinburgh based corporate branding. I have done my M.Com in Marketing &amp; Finance from Eastmoor University. I live in Musselburgh with my wife and daughter.</p>
  <h3 class="abs skills-title" style="top:138px">What I can Do</h3>

  <div class="abs skill" style="top:218px">
    <svg width="52" height="44" viewBox="0 0 52 44" fill="none" stroke="#fff" stroke-width="2"><rect x="8" y="4" width="36" height="26" rx="2"/><path d="M20 38h12M26 30v8M15 22l8-8 6 5 9-9"/></svg>
    <div><h3>BRAND MARKETING</h3><p>I build abstract representation of a real world branding concept using complex behavioral habits &amp; consumer based tools.</p></div>
  </div>
  <div class="abs skill" style="top:324px">
    <svg width="52" height="44" viewBox="0 0 52 44" fill="none" stroke="#fff" stroke-width="2"><rect x="6" y="8" width="40" height="28"/><path d="M6 8l20 16 20-16"/></svg>
    <div><h3>EMAIL AUTOMATION</h3><p>I provide clients with email setup and automation services, depending on their business and preferences.</p></div>
  </div>
  <div class="abs skill" style="top:430px">
    <svg width="52" height="44" viewBox="0 0 52 44" fill="none" stroke="#fff" stroke-width="2"><rect x="4" y="6" width="44" height="32" rx="2"/><path d="M4 13h44M19 20l-6 6 6 6M33 20l6 6-6 6M28 19l-4 14"/></svg>
    <div><h3>WEB DEVELOPING</h3><p>I have managed several web developing projects of my clients while I implement branding strategies and monitor portfolio.</p></div>
  </div>
  <div class="abs skill" style="top:538px">
    <svg width="52" height="44" viewBox="0 0 52 44" fill="none" stroke="#fff" stroke-width="2"><rect x="6" y="6" width="40" height="32"/><path d="M14 30V22M22 30V16M30 30V20M38 30V12"/></svg>
    <div><h3>BUSINESS CONSULTING</h3><p>I have conducted several business consulting programs where I guide people in developing their business growth.</p></div>
  </div>
</section>

<section class="section timeline">
  <h2 class="abs timeline-title">Timeline</h2>
  <div class="abs year-big">2013</div>
  <div class="abs years"><span>2010</span><span>2011</span><span>2012</span><span style="width:60px"></span><span>2014</span><span>2015</span><span>2016</span></div>
  <svg class="abs ticks" viewBox="0 0 470 30" stroke="#5c6675" stroke-width="2"><path d="M0 0v22M72 0v22M146 0v22M292 0v22M364 0v22M440 0v22"/><path d="M218 0v22" stroke="#2f86dc" stroke-width="3"/></svg>
  <div class="abs org-mark"><i></i>HALVERN</div>
  <div class="abs job">
    <h3>HALVERN INC. <small>(till Dec 2015)</small></h3>
    <h4>Brand Manager</h4>
    <p>HALVERN UK was the first top 500 global company in my career. Here my responsibility was to ensure that firm is able to continue its operations and that it has sufficient ability to satisfy both maturing short-term debt and upcoming operational expenses.</p>
    <a href="#">Download Resume</a>
  </div>
</section>

<section class="section feed">
  <article class="abs post" style="left:112px">
    <div class="post-head post-head-top"><i></i></div>
    <div class="post-head" style="margin-bottom:10px">Chatter <time>2017-09-03 09:22PM</time></div>
    <p>Brexit to blame for over $81 billion worth of missed investment opportunities. Report via @BNW<br>#Brexit #Investment</p>
  </article>
  <article class="abs post" style="left:460px">
    <div class="post-head post-head-top"><i></i></div>
    <div class="post-head" style="margin-bottom:10px">Friendwall <time>2017-09-03 09:22PM</time></div>
    <p>Budget is the first step to gain some financial order in your home.<br>#Budget #Finance #planning<br>www.weekendfolk.example/finance</p>
  </article>
  <article class="abs post raised" style="left:805px">
    <div class="post-head post-head-top"><i></i></div>
    <div class="post-head" style="margin-bottom:10px">WorkLink <time>2017-09-03 09:22PM</time></div>
    <p>CEOs connect with hundreds of people daily. Yet only some interactions—and individuals—stand out as relevant and wise. For me, the difference between…</p>
  </article>
  <div class="abs feed-dots"><span></span><span class="on"></span><span></span></div>
</section>

<section class="section memory">
  <h2 class="abs memory-title">Happy Memory</h2>
  <nav class="abs memory-tabs"><span>Hiking</span><span>Rock Climbing</span><span>Traveling</span><span>Exercising and Transformation</span>
    <svg width="18" height="12" viewBox="0 0 18 12" fill="none" stroke="#fff" stroke-width="2"><path d="M0 6h16M11 1l5 5-5 5"/></svg></nav>
  <div class="abs photo" style="left:0;width:70px;background:linear-gradient(180deg,#8ab0d6,#4f7a55 60%,#3b5b3a)" role="img" aria-label="Coastal cliffs with green hills"></div>
  <div class="abs photo" style="left:112px;width:297px;background:linear-gradient(180deg,#3c4e66,#2c3a4d)" role="img" aria-label="Cathedral in Italy under a dark blue overlay">
    <div class="abs photo-caption"><h3>ITALY</h3><p>in August 2016 - 50 Photos</p><a href="#">View the Gallery</a></div>
  </div>
  <div class="abs photo" style="left:450px;width:298px;background:linear-gradient(180deg,#c9d9ea 0%,#dfe6ee 45%,#9aa3ab 100%)" role="img" aria-label="Glass pyramid in front of a museum courtyard"></div>
  <div class="abs photo" style="left:790px;width:298px;background:linear-gradient(180deg,#8fb4de 0%,#5d5a55 45%,#3a3230 100%)" role="img" aria-label="Ornate temple gate with visitors"></div>
  <div class="abs photo" style="left:1128px;width:72px;background:linear-gradient(180deg,#9bbbd8,#6c7a4a 60%,#4a5a34)" role="img" aria-label="Historic stone building among trees"></div>
  <svg class="abs arrow" style="left:112px" width="36" height="20" viewBox="0 0 36 20" fill="none" stroke="#fff" stroke-width="3"><path d="M34 10H4M12 2l-8 8 8 8"/></svg>
  <svg class="abs arrow" style="left:1052px" width="36" height="20" viewBox="0 0 36 20" fill="none" stroke="#fff" stroke-width="3"><path d="M2 10h30M24 2l8 8-8 8"/></svg>
</section>

<section class="section journal">
  <h2 class="abs journal-title">My Journal</h2>
  <a class="abs all-posts" href="#">All Posts &#8594;</a>

  <article class="abs card" style="left:112px;top:190px;width:297px;height:446px">
    <div style="height:212px;background:linear-gradient(160deg,#7a4a2c,#b8732f 50%,#5e7a3a)" role="img" aria-label="Plated vegan burger with fresh vegetables"></div>
    <div style="padding:24px 26px">
      <h3>How to Eat Around the World on a Vegan Diet</h3>
      <div class="meta"><span>May 07, 2017</span><span>&#9829; 29 &nbsp; &#9670; 29</span></div>
      <p>Fifty days ago, India yanked most of its currency from circulation without warning, jolting the economy and leaving most citizens scrambling for cash.</p>
    </div>
  </article>

  <article class="abs card" style="left:450px;top:190px;width:298px;height:208px;padding:24px 26px">
    <h3>How to Travel with a Theme Pack</h3>
    <div class="meta"><span>May 07, 2017</span><span>&#9829; 5 &nbsp; &#9670; 10</span></div>
    <p>Several countries are undergoing "demonetization" or currency reforms in which the government…</p>
  </article>
  <article class="abs card" style="left:450px;top:428px;width:298px;height:208px;padding:24px 26px">
    <h3>Is Europe Safe to Visit Right Now?</h3>
    <div class="meta"><span>May 07, 2017</span><span>&#9829; 10 &nbsp; &#9670; 45</span></div>
    <p>Marcus Delvin bet that his team of followers could beat the market. Reckons that the cost of his wealth is in Corwick Holdings…</p>
  </article>

  <article class="abs card feature-dark" style="left:790px;top:190px;width:298px;height:446px;background:linear-gradient(180deg,#5d5a57,#3f3c3a)" role="img" aria-label="Traveller reading a paper map, under a dark overlay">
    <div style="padding:24px 26px">
      <h3>Finding a Map for Saturday: 10 Years Later</h3>
      <div class="meta"><span>May 07, 2017</span><span>&#9829; 58 &nbsp; &#9670; 112</span></div>
      <p>Marcus Delvin, who has recently joined the Thornwell Institute as a visiting fellow, and Ada Korvel have a new working paper out titled Declining Entrepreneurship, Labor Mobility, and Business Dynamism: A Demand-side Approach.</p>
      <p style="margin-top:14px">We hope you check it out! We think it adds some important evidence to an ambitious debate. Here is a great writeup by Lena Hart at The Daily Ledger Journal this morning.</p>
      <a href="#" style="display:inline-block;margin-top:16px;font-size:13px;font-weight:500;color:#fff;border-bottom:2px solid var(--blue-bright);padding-bottom:4px">Full Post</a>
    </div>
  </article>
</section>

<section class="section stats">
  <div class="abs stat" style="left:98px">
    <svg width="44" height="60" viewBox="0 0 44 60" fill="none" stroke="#fff" stroke-width="2"><path d="M10 4h24v14a12 12 0 0 1-24 0z"/><path d="M10 9H3a7 7 0 0 0 7 9M34 9h7a7 7 0 0 1-7 9M22 30v14M12 56h20l-3-12H15z"/></svg>
    <h3>2 Times BFM</h3><p>2 times Best Brand Manager in<br>Edinburgh in last 3 years</p>
  </div>
  <div class="abs stat" style="left:382px">
    <svg width="64" height="60" viewBox="0 0 64 60" fill="none" stroke="#fff" stroke-width="2"><path d="M4 26l14-12 12 6 10-6 20 12M18 14l-14 12 14 16h8l12 8 16-18M26 26l12 10M22 32l10 8M18 38l8 6"/></svg>
    <h3>350 Customers</h3><p>I have worked over 350 clients in last<br>5 years on Brand Promotion</p>
  </div>
  <div class="abs stat" style="left:660px">
    <svg width="66" height="60" viewBox="0 0 66 60" fill="none" stroke="#fff" stroke-width="2"><path d="M4 24h58M8 24l2 14h16l3-14M37 24l3 14h16l2-14M29 28h8"/></svg>
    <h3>50,000 Subscriber</h3><p>That's the number of people regularly<br>read my journal</p>
  </div>
  <div class="abs stat" style="left:932px">
    <svg width="44" height="60" viewBox="0 0 44 60" fill="none" stroke="#fff" stroke-width="2"><path d="M22 56s-14-18-14-30a14 14 0 0 1 28 0c0 12-14 30-14 30z"/><circle cx="22" cy="25" r="5"/></svg>
    <h3>Traveled 100 Places</h3><p>List includes Solmar Bay Resort, Jeju<br>Island, Pamukkale and many more</p>
  </div>
</section>

<footer class="section footer">
  <h2 class="abs" style="left:112px;top:56px">I am</h2>
  <div class="abs name" style="left:112px;top:100px">Your Name Here</div>
  <div class="abs role" style="left:112px;top:152px">Brand Manager &amp; Travel Enthusiast</div>
  <div class="abs footer-social"><i class="dot-icon"></i><i class="dot-icon"></i><i class="dot-icon"></i><i class="dot-icon"></i></div>
  <div class="abs subscribe">
    <h4>Subscribe Me</h4>
    <div class="field">your email address</div>
    <div class="contact">Contact<br>14 Quarry Lane, Edinburgh EH9 2QX,<br>UK<br>+44 000 555 0142 &nbsp;| +44 000 555 0199</div>
  </div>
</footer>

</body>
</html>
```